creative design for packing box of 3D paper puzzle

We want to get a packaging box design for the 3D puzzle. The packaging is for animal puzzles, like birds, insect ,wild animal. it is for young chirdren. 5-12 years old.
The box size : 12*17*2CM, 2.5CM header. Attach is some packing design ideal and our logo.
We like more nice design. It can attract the eyes. We hope all items can be use same background, and just change the color and put different animal photo on it. Box is same design, you can check the file “box-different color” . same design, just diffirent color, photo, text..
Please send us your design in diffirent color. Also You can visit our website: www.tovel.com. you can kow how about our product.
We attach 3 items photo. You can choose one to make the designon. Our product is DIY, education. Animal with scene
Target Market(s)
Europe,Janpan,USA
Colors
Designer to choose colors to be used in the design.
Requirements
Must have
- our Logo, some nice text or signo
Nice to have
- nice background

```html
<!DOCTYPE html>
<html lang="en">
<head>
<meta charset="utf-8">
<title>3D Paper Puzzle – Triceratops box</title>
<link href="https://fonts.googleapis.com/css2?family=Varela+Round&display=swap" rel="stylesheet">
<style>
  :root{
    --bg:#f1f1f2;
    --yellow:#f6bd2a;
    --orange:#ec6a1c;
    --green:#a6c266;
    --blue:#1f4f9c;
    --white:#ffffff;
    --photo-bg:#e9e9eb;
  }
  html,body{margin:0;padding:0;overflow:hidden;}
  body{
    width:1200px;height:1200px;background:var(--bg);
    font-family:"Varela Round",sans-serif;
    position:relative;
  }
  .box{position:absolute;left:215px;top:69px;width:770px;height:1062px;display:flex;}

  /* spine */
  .box-spine{position:relative;width:120px;height:100%;background:var(--yellow);overflow:hidden;}
  .spine-series{
    position:absolute;left:0;top:0;width:100%;height:330px;background:var(--orange);
  }
  .spine-text{
    position:absolute;left:50%;color:var(--white);white-space:nowrap;
    transform:translateX(-50%) rotate(90deg);transform-origin:center;
  }
  .spine-series .spine-text{top:150px;font-size:50px;letter-spacing:2px;}
  .spine-title{top:680px;font-size:48px;letter-spacing:16px;}

  /* front */
  .box-front{position:relative;width:650px;height:100%;background:var(--photo-bg);overflow:hidden;}
  .brand-block{
    position:absolute;left:0;top:0;width:243px;height:270px;background:var(--white);
    display:flex;flex-direction:column;align-items:center;justify-content:center;gap:16px;
  }
  .brand-dot{width:100px;height:100px;border-radius:50%;background:var(--blue);}
  .brand-name{color:var(--blue);font-size:30px;letter-spacing:4px;}
  .title-block{
    position:absolute;left:243px;top:0;right:0;height:270px;background:var(--yellow);
    color:var(--white);text-align:right;padding-right:24px;box-sizing:border-box;
    display:flex;flex-direction:column;justify-content:center;align-items:flex-end;
  }
  .title-3d{font-size:60px;line-height:1;margin-bottom:26px;}
  .title-main{font-size:40px;letter-spacing:2px;line-height:1;white-space:nowrap;}
  .ages{position:absolute;left:36px;top:284px;color:var(--blue);font-size:18px;letter-spacing:1.5px;}
  .product-photo{
    position:absolute;left:60px;top:320px;width:560px;height:500px;border-radius:60px;
    background:radial-gradient(ellipse at 50% 48%, #a5d46a 0%, #6a9a50 30%, #c27a2a 58%, rgba(233,233,235,0) 72%);
  }
  .product-name{position:absolute;right:36px;top:750px;text-align:right;color:var(--blue);}
  .product-name .animal{font-size:30px;letter-spacing:1.5px;display:block;line-height:1.15;}
  .product-name .sub{font-size:20px;letter-spacing:1px;}
  .yellow-strip{position:absolute;left:0;right:0;top:840px;height:22px;background:var(--yellow);}
  .green-base{position:absolute;left:0;right:0;top:862px;bottom:0;background:var(--green);}
  .series-label{
    position:absolute;left:227px;top:867px;width:240px;height:100px;background:var(--orange);
    color:var(--white);font-size:42px;display:flex;align-items:center;justify-content:center;letter-spacing:1px;
  }
</style>
</head>
<body>
  <div class="box">
    <aside class="box-spine">
      <div class="spine-series"><span class="spine-text">animals</span></div>
      <span class="spine-text spine-title">3D PAPER PUZZLE</span>
    </aside>
    <main class="box-front">
      <div class="brand-block">
        <div class="brand-dot"></div>
        <div class="brand-name">PAPIKO</div>
      </div>
      <div class="title-block">
        <div class="title-3d">3D</div>
        <div class="title-main">PAPER PUZZLE</div>
      </div>
      <div class="ages">AGES: 5 - 12</div>
      <div class="product-photo" role="img" aria-label="Photo of the assembled green paper triceratops model standing on an orange base with palm trees"></div>
      <div class="product-name">
        <span class="animal">TRICERATOPS</span>
        <span class="sub">with scene</span>
      </div>
      <div class="yellow-strip"></div>
      <div class="green-base"></div>
      <div class="series-label">animals</div>
    </main>
  </div>
</body>
</html>
```